Brochure Design Project A5 (UK) 64 pages apox Making Money From Financial Trading

I require a website (long sales letter) turned into a A5 booklet for mailing out will will be full colour. You must provide a complete end to end to service, I will provide all the text and photos and you need to layout and design the brochure, resize photos to fit. I see the size being around 64 sides of UK A5 paper
148 x 210mm 5.83 x 8.27

You must be creative with text layout and typography, this is very text heavy over 10,000 words in to total. the website can be seen at www.gildenmarsh-ledger.com however this is NOT the final text but gives you an idea. (I have attached 5 pages of text)

They typical reader is male over 40, it needs to be readable, experience with magazine layouts and advantage

The finished project must be ready to go to print.

So it needs a front and back cover designed - I have attached a sample DVD cover as an idea from one of our products and then the inside pages, designed/set out

We have made the project guaranteed so step up and give me your best designs

Reason: Dear All. The standard of work submitted so far has been very poor and amateurish. We have decided to use another company for the front and back cover, therefore leaving you to concentrate on the text for inside the booklet. If you wish to resubmit some better designs then please go ahead. Thx

Target Market(s)

The typical client is Male, professional, looking make money from the stockmarket. The end user already knows the author

Industry/Entity Type

Financial

Requirements
Must have
• Must have good and creative typography

```html
<!DOCTYPE html>
<html lang="en">
<head>
<meta charset="utf-8">
<title>Trading Booklet – Pages 5 and 6</title>
<link href="https://fonts.googleapis.com/css2?family=Tinos:ital,wght@0,400;0,700;1,400&family=Arimo:ital,wght@0,700;1,700&display=swap" rel="stylesheet">
<style>
  :root {
    --paper: #ffffff;
    --ink: #1a1a1a;
    --accent-blue: #00a3e8;
    --rule-grey: #cfcfcf;
    --edge: #222222;
  }
  html, body {
    margin: 0;
    padding: 0;
    width: 1200px;
    height: 850px;
    overflow: hidden;
    background: var(--paper);
  }
  .spread {
    position: relative;
    width: 1200px;
    height: 850px;
    background: var(--paper);
    color: var(--ink);
    font-family: "Tinos", "Times New Roman", serif;
    font-size: 15.5px;
    line-height: 24px;
    overflow: hidden;
  }
  .page-edge {
    position: absolute;
    top: 0;
    height: 850px;
    border-left: 1.5px solid var(--edge);
  }
  .page-edge--left { left: 0; }
  .page-edge--gutter { left: 600px; }
  .page-edge--right { left: 1198px; }
  .page-number {
    position: absolute;
    top: 10px;
    font-family: "Arimo", Arial, sans-serif;
    font-weight: 700;
    font-size: 16px;
    line-height: 20px;
  }
  .page-number--left { left: 40px; }
  .page-number--right { right: 40px; }
  .header-band {
    position: absolute;
    top: 139px;
    left: 40px;
    width: 1119px;
    height: 11px;
    background: var(--accent-blue);
  }
  .divider-bar {
    position: absolute;
    top: 309px;
    left: 664px;
    width: 495px;
    height: 9px;
    background: var(--rule-grey);
  }
  .text-block {
    position: absolute;
    text-align: justify;
  }
  .text-block p { margin: 0 0 16px; }
  .left-page-copy { top: 166px; left: 40px; width: 496px; }
  .right-page-intro { top: 156px; left: 664px; width: 495px; }
  .column-one { top: 335px; left: 664px; width: 233px; }
  .column-two { top: 335px; left: 931px; width: 228px; }
  .testimonial { font-style: italic; }
  .testimonial-name { font-style: normal; font-weight: 700; }
  .section-heading {
    font-family: "Arimo", Arial, sans-serif;
    font-style: italic;
    font-weight: 700;
    font-size: 19px;
    line-height: 24px;
    margin: 2px 0 16px;
    text-align: left;
  }
</style>
</head>
<body>
<main class="spread">
  <div class="page-edge page-edge--left"></div>
  <div class="page-edge page-edge--gutter"></div>
  <div class="page-edge page-edge--right"></div>

  <span class="page-number page-number--left">5</span>
  <span class="page-number page-number--right">6</span>

  <div class="header-band"></div>

  <section class="text-block left-page-copy">
    <p>trading account has made money every single year for the last 14 years. Of course, I have losing weeks and months, but I have never had a losing year.</p>
    <p>Take for example what’s happened to Martin Haworth:</p>
    <p class="testimonial">“After an amazing few months and since my original attendance at your trading day, I have made over £50,000.00! I wanted to take a couple of minutes to thank you for all your help and advice. I always thought your comments sounded too good to be true, however, the results when I finally took the plunge and attended your course, have been incredible and I am most grateful to you for your persistence and for all you that you have taught me since. Many thanks and best regards.” <span class="testimonial-name">(Martin Haworth).</span></p>
    <p>Or see what Carol Finchley and Dennis Alwyn had to say about the workshop:</p>
    <p class="testimonial">“Wow! What can I say; that was a MIND-BLOWING day on Friday. Dennis and I thoroughly enjoyed the learning experience. The last hour was absolutely amazing. It is awesome to think that you made in a few minutes twice what Dennis makes working an 83 hour week!! You can’t imagine what these extra earnings will mean to our company. Dennis and I thank you once again for a fantastically informative day.” <span class="testimonial-name">(Carol Finchley and Dennis Alwyn).</span></p>
    <p>Then there was Graham Pellow...</p>
    <p class="testimonial">“I have had a great year and am up £230K to the 11th July when I closed 90% of my trades and went to New Zealand. I have only started back trading today, and I feel more relaxed and more confident than ever.” <span class="testimonial-name">(Graham Pellow).</span></p>
  </section>

  <section class="text-block right-page-intro">
    <p>And let’s not forget Ravi Dhanda from Leicester...</p>
    <p class="testimonial">“I went from knowing little about trading at 9.30am Friday to making just over £5,000 total profit tax-free by the close of business on Monday – to say I am delighted is an understatement. Attending this event was the most profitable and rewarding thing I have ever done.” <span class="testimonial-name">(Ravi Dhanda).</span></p>
  </section>

  <div class="divider-bar"></div>

  <section class="text-block column-one">
    <p>I could go on, but I think you get the idea. It’s important to note that none the above had trading experience before they became my students; they all came from non-investing or trading backgrounds, but were involved in professions and being business owners such as vets, dentists, doctors, accountants, florist owner, London back cab driver, farmer, airline pilot, lawyers, and even a gentleman that owns a remote salmon fish farm.</p>
    <h2 class="section-heading">Why this is different?</h2>
    <p>I come from the school of hard knocks. I am not scared of taking the opposite view to the crowd or making hard decisions. I am not commissioned by bookmakers or</p>
  </section>

  <section class="text-block column-two">
    <p>brokers and I am results driven and tell you how it really is, even if sometimes you don’t want to hear it.</p>
    <p>I quickly learnt that if you do what everyone else does, you will get the same results and as 90% of traders and investors don’t make money and that includes all the so called professionals, I did not want to be with the masses.</p>
  </section>
</main>
</body>
</html>
```